Brightmoor Advisory

Looking for modern business cards.
Clean contemporary design.
Similar to this.
https://www.quorvexsearch.example/imgview?src=https%3A%2F%2Fimg.pellumcards.example%2Fprofessional_elegant_modern_black_plain_metal_business_card-a7c21e90b4d3f5e6a8b9c0d1e2f3a4b5_540.jpg&ref=https%3A%2F%2Fwww.pellumcards.example%2Fprofessional_elegant_modern_black_plain_metal_business_card-518273640192837465&id=7kQ2mZ9x-PL4TW&w=540&h=540&q=modern%20business%20cards

But I'd like the blue to look metallic.

```html
<!DOCTYPE html>
<html lang="en">
<head>
<meta charset="utf-8">
<title>Brightmoor Advisory – Business Card</title>
<link href="https://fonts.googleapis.com/css2?family=Lato:ital,wght@0,400;0,700;1,700&display=swap" rel="stylesheet">
<style>
  :root {
    --page: #e6e9ec;
    --metal-base: #4a93b3;
    --metal-light: #5aa3c2;
    --metal-dark: #3f86a6;
    --navy: #1d3d6e;
    --ink: #1f3b63;
    --sky: #2bb4ef;
    --white: #ffffff;
    --mail-ink: #2b4b60;
  }
  * { margin: 0; padding: 0; box-sizing: border-box; }
  html, body { width: 1200px; height: 1200px; overflow: hidden; }
  body {
    background: var(--page);
    font-family: "Lato", Arial, sans-serif;
    position: relative;
  }
  .card {
    position: absolute;
    left: 212px;
    width: 776px;
    height: 430px;
    overflow: hidden;
    background:
      repeating-linear-gradient(0deg, rgba(255,255,255,0.05) 0 1px, rgba(0,0,0,0.03) 1px 2px, transparent 2px 4px),
      linear-gradient(100deg, rgba(255,255,255,0.10) 0%, rgba(255,255,255,0) 30%, rgba(255,255,255,0.14) 55%, rgba(0,0,0,0.06) 80%, rgba(255,255,255,0.08) 100%),
      linear-gradient(180deg, var(--metal-light), var(--metal-base) 45%, var(--metal-dark));
    box-shadow: 0 2px 6px rgba(0,0,0,0.18);
  }
  .card--front { top: 113px; }
  .card--back { top: 656px; }

  /* Front */
  .front-name {
    position: absolute;
    left: 100px;
    top: 180px;
    font-size: 54px;
    font-weight: 700;
    color: var(--white);
    letter-spacing: -0.5px;
    white-space: nowrap;
  }
  .front-mark {
    position: absolute;
    left: 640px;
    top: 196px;
    width: 34px;
    height: 34px;
    border-radius: 50%;
    background: var(--white);
  }
  .front-tagline {
    position: absolute;
    left: 234px;
    top: 248px;
    font-size: 13px;
    font-style: italic;
    font-weight: 700;
    letter-spacing: 2px;
    color: var(--white);
    white-space: nowrap;
  }
  .front-email {
    position: absolute;
    left: 208px;
    top: 318px;
    font-size: 17px;
    letter-spacing: 3.5px;
    color: var(--mail-ink);
    white-space: nowrap;
  }

  /* Back */
  .strip {
    position: absolute;
    left: 410px;
    width: 30px;
    background: var(--navy);
  }
  .strip--top { top: 0; height: 64px; }
  .strip--bottom { top: 116px; bottom: 0; border-radius: 15px 15px 0 0; }

  .back-brand {
    position: absolute;
    left: 48px;
    top: 210px;
    font-size: 28px;
    font-weight: 700;
    color: var(--navy);
    white-space: nowrap;
  }
  .back-tagline {
    position: absolute;
    left: 122px;
    top: 248px;
    font-size: 7px;
    font-style: italic;
    font-weight: 700;
    letter-spacing: 1px;
    color: var(--white);
    white-space: nowrap;
  }
  .person {
    position: absolute;
    left: 462px;
    top: 60px;
  }
  .person-name {
    font-size: 29px;
    font-weight: 700;
    color: var(--sky);
    line-height: 1;
  }
  .person-role {
    font-size: 20px;
    color: var(--ink);
    line-height: 1.1;
  }
  .contact-list { list-style: none; }
  .contact {
    position: absolute;
    left: 410px;
    display: flex;
    align-items: center;
    height: 30px;
  }
  .contact-icon {
    width: 30px;
    height: 30px;
    border-radius: 50%;
    background: var(--navy);
    display: flex;
    align-items: center;
    justify-content: center;
  }
  .contact-icon svg { width: 16px; height: 16px; }
  .contact-text {
    margin-left: 11px;
    font-size: 15px;
    color: var(--ink);
    white-space: nowrap;
  }
</style>
</head>
<body>

<section class="card card--front" aria-label="Card front">
  <div class="front-name">Brightmoor Advisory</div>
  <div class="front-mark" aria-hidden="true"></div>
  <div class="front-tagline">“Steady Counsel for Companies on the Rise”</div>
  <div class="front-email">elias@brightmooradvisory.com</div>
</section>

<section class="card card--back" aria-label="Card back">
  <div class="strip strip--top"></div>
  <div class="strip strip--bottom"></div>

  <div class="back-brand">Brightmoor Advisory</div>
  <div class="back-tagline">“Steady Counsel for Companies on the Rise”</div>

  <div class="person">
    <div class="person-name">Elias Varnholt</div>
    <div class="person-role">Managing Partner</div>
  </div>

  <ul class="contact-list">
    <li class="contact" style="top:153px">
      <span class="contact-icon">
        <svg viewBox="0 0 24 24"><path fill="#2bb4ef" d="M6.6 10.8a15 15 0 0 0 6.6 6.6l2.2-2.2c.3-.3.7-.4 1-.2 1.1.4 2.3.6 3.6.6.6 0 1 .4 1 1V20c0 .6-.4 1-1 1A17 17 0 0 1 3 4c0-.6.4-1 1-1h3.5c.6 0 1 .4 1 1 0 1.3.2 2.5.6 3.6.1.3 0 .7-.2 1z"/></svg>
      </span>
      <span class="contact-text">323 555 0148</span>
    </li>
    <li class="contact" style="top:203px">
      <span class="contact-icon">
        <svg viewBox="0 0 24 24"><path fill="#ffffff" d="M2 9c3-3 17-3 20 0v2h-5V9c-2-1-8-1-10 0v2H2z"/><rect x="5" y="12" width="14" height="7" rx="1.5" fill="#ffffff"/><circle cx="12" cy="15.5" r="2" fill="#1d3d6e"/></svg>
      </span>
      <span class="contact-text">888 555 0172</span>
    </li>
    <li class="contact" style="top:248px">
      <span class="contact-icon">
        <svg viewBox="0 0 24 24"><rect x="7" y="3" width="10" height="5" fill="#ffffff"/><rect x="3" y="8" width="18" height="8" rx="1.5" fill="#ffffff"/><rect x="7" y="13" width="10" height="8" fill="#ffffff" stroke="#1d3d6e" stroke-width="1.5"/></svg>
      </span>
      <span class="contact-text">800 555 0193</span>
    </li>
    <li class="contact" style="top:291px">
      <span class="contact-icon">
        <svg viewBox="0 0 24 24"><rect x="3" y="6" width="18" height="12" fill="none" stroke="#ffffff" stroke-width="1.8"/><path d="M3 6l9 7 9-7" fill="none" stroke="#ffffff" stroke-width="1.8"/></svg>
      </span>
      <span class="contact-text">elias@brightmooradvisory.com</span>
    </li>
    <li class="contact" style="top:337px">
      <span class="contact-icon">
        <svg viewBox="0 0 24 24" fill="none" stroke="#ffffff" stroke-width="1.6"><circle cx="12" cy="12" r="9"/><ellipse cx="12" cy="12" rx="4" ry="9"/><path d="M3 12h18M5 7h14M5 17h14"/></svg>
      </span>
      <span class="contact-text">www.brightmooradvisory.com</span>
    </li>
  </ul>
</section>

</body>
</html>
```